Hip surgeon needs a stationery design

I need a new stationery design for my private practice.
My practice is focused in hip arthroplasty (hip prosthesis).
I'd like to see designs most in blue or shades of blue.
I've uploaded my new logo to help with the task.
Also, I'm a member of some societies and I've uploaded their logos either, so I'd like to see them in some of the stationeries.
Itens list:
business card
letterhead A4
envelope
prescription block A5
one fold for A4 (please see the archive "pocket")
Personal data:
Dr. Renato L. Ferraz
CRM/PR 73915
site: www.clinicaarticular.com.br
email: dr.renato@clinicaarticular.com.br
Adress:
Rua Benedito Almeida Prates, 912
Campo Alegre - Curitiba/PR
41 35718206 I 35718207
Updates
I forgot to mention that my practice is focused primarily in hip arthroplasty (total hip prosthesis) and the target audience range from young adults to the elderly.
I also perform hip preserving surgeries (open and arthroscopic procedures) and pelvic and hip fracture surgery (trauma).
- Any "cleaner" fonts are welcome

```html
<!DOCTYPE html>
<html lang="pt-BR">
<head>
<meta charset="utf-8">
<title>Papel timbrado — Dr. Renato L. Ferraz</title>
<link href="https://fonts.googleapis.com/css2?family=Carlito:wght@400&family=Roboto+Condensed:wght@400;500&family=Arimo:wght@400&display=swap" rel="stylesheet">
<style>
  :root {
    --backdrop: #e6e6e6;
    --paper: #f6f6f6;
    --sidebar: #ebebeb;
    --brand-blue: #1c6db3;
    --text: #3a3a3a;
    --contact-text: #555a60;
    --rule: #9aa6b4;
    --watermark: #e2e2e2;
    --badge: #b9babd;
  }
  * { margin: 0; padding: 0; box-sizing: border-box; }
  html, body {
    width: 1200px;
    height: 1050px;
    overflow: hidden;
    background: var(--backdrop);
  }
  .canvas {
    position: relative;
    width: 1200px;
    height: 1050px;
  }
  .letterhead {
    position: absolute;
    left: 228px;
    top: 46px;
    width: 744px;
    height: 958px;
    background: var(--paper);
    overflow: hidden;
    box-shadow: 0 2px 10px rgba(0,0,0,0.12);
  }
  .letterhead__sidebar {
    position: absolute;
    left: 634px;
    top: 0;
    width: 110px;
    height: 100%;
    background: var(--sidebar);
  }
  .letterhead__watermark {
    position: absolute;
    left: 500px;
    top: 703px;
    width: 250px;
    height: 250px;
    border-radius: 50%;
    background: var(--watermark);
  }
  .letterhead__baseline {
    position: absolute;
    left: 0;
    bottom: 0;
    width: 100%;
    height: 5px;
    background: var(--brand-blue);
  }
  .brand {
    position: absolute;
    left: 62px;
    top: 48px;
    display: flex;
    align-items: center;
    gap: 10px;
  }
  .brand__mark {
    width: 56px;
    height: 56px;
    border-radius: 50%;
    border: 6px solid var(--brand-blue);
  }
  .brand__name {
    font-family: "Roboto Condensed", sans-serif;
    font-weight: 500;
    font-size: 26px;
    line-height: 1.05;
    color: var(--brand-blue);
  }
  .brand__specialty {
    font-family: "Roboto Condensed", sans-serif;
    font-weight: 400;
    font-size: 19px;
    line-height: 1.15;
    color: var(--brand-blue);
  }
  .society-badge {
    position: absolute;
    left: 648px;
    top: 52px;
    width: 34px;
    height: 34px;
    border-radius: 50%;
    background: var(--badge);
  }
  .letter-body {
    position: absolute;
    left: 62px;
    top: 166px;
    width: 559px;
    font-family: "Carlito", sans-serif;
    font-size: 13.2px;
    line-height: 20px;
    color: var(--text);
    text-align: justify;
  }
  .letter-body p { margin-bottom: 20px; }
  .letter-body p.after-gap { margin-top: 20px; }
  .letter-body .closing { margin-top: 42px; text-align: left; }
  .contact {
    position: absolute;
    left: 646px;
    top: 831px;
    width: 92px;
    font-family: "Arimo", sans-serif;
    font-size: 10.2px;
    line-height: 11.5px;
    color: var(--contact-text);
  }
  .contact__rule {
    width: 82px;
    height: 1px;
    background: var(--rule);
    margin-bottom: 26px;
  }
  .contact__line { display: flex; align-items: center; gap: 4px; white-space: nowrap; }
  .contact__icon { width: 8px; height: 8px; flex: none; }
  .contact__icon path, .contact__icon rect { fill: none; stroke: var(--brand-blue); stroke-width: 1.2; }
</style>
</head>
<body>
<main class="canvas">
  <article class="letterhead">
    <div class="letterhead__sidebar"></div>
    <div class="letterhead__watermark"></div>

    <header class="brand">
      <span class="brand__mark"></span>
      <div>
        <div class="brand__name">Dr. Renato L. Ferraz</div>
        <div class="brand__specialty">Cirurgia do Quadril</div>
      </div>
    </header>

    <span class="society-badge"></span>

    <section class="letter-body">
      <p>Lorem ipsum dolor sit amet, consectetur adipiscing elit. Duis sed aliquet neque. Fusce mollis placerat leo eu faucibus. Suspendisse suscipit egestas nunc, consequat euismod quam elementum venenatis. Nulla vitae nulla id mauris dictum imperdiet in vitae augue. Suspendisse fringilla bibendum ultrices.</p>
      <p>Sed rhoncus, nisi nec egestas tempus, orci velit ullamcorper dolor, malesuada molestie libero tellus in justo. Duis pharetra, turpis vel ultrices consequat, est ante laoreet nisi, et imperdiet ligula ipsum non quam. In tristique consequat diam, sed semper dolor aliquet et. Cum sociis natoque penatibus et magnis dis parturient montes, nascetur ridiculus mus. Duis sit amet ante mauris, a sodales tellus. Phasellus ante eros, lacinia at eleifend eu, laoreet sed nibh. Nulla rhoncus erat vitae dolor aliquam varius pretium lectus accumsan.</p>
      <p class="after-gap">Aliquam quis lorem eget nibh dignissim accumsan. Proin vitae lectus pretium justo molestie pellentesque. Fusce ultrices risus vitae justo adipiscing id consectetur elit sagittis. Integer nec dapibus tellus. Donec ultricies massa a dolor eleifend ut adipiscing felis feugiat. Praesent fermentum sem felis, vitae vulputate odio. Curabitur faucibus leo quis velit molestie in fringilla ligula mollis. Pellentesque aliquet dolor ut nibh tempor sed vehicula arcu malesuada. Maecenas eget justo at augue molestie ullamcorper non eu est. Cras varius ullamcorper malesuada. Proin ut enim imperdiet augue pulvinar iaculis eget nec ipsum. Fusce sed orci mi. Etiam tristique suscipit ligula non volutpat. Nullam lobortis, enim sed faucibus faucibus, lacus risus euismod ligula, at interdum justo libero a elit. Pellentesque sem ligula, tempor a faucibus auctor, gravida et ante. Donec tristique imperdiet eros et vulputate. Cras id purus id mi volutpat egestas. Cras tellus velit, tristique at dignissim et, tincidunt at felis. Maecenas vestibulum felis eget mauris pellentesque gravida. Nunc commodo tincidunt ornare. Suspendisse quis volutpat lectus. Nunc sed dui sit amet nulla vulputate congue et imperdiet mi.</p>
      <p class="closing">Sincerely</p>
    </section>

    <address class="contact" style="font-style:normal">
      <div class="contact__rule"></div>
      <div class="contact__line">Co. Street, Building</div>
      <div class="contact__line">Suite 8100</div>
      <div class="contact__line">City/State, Zip Code</div>
      <div class="contact__line">
        <svg class="contact__icon" viewBox="0 0 8 8"><path d="M1 2.5 Q4 0.5 7 2.5 L6 4 L5 3.5 L3 3.5 L2 4 Z M2 4 L2 7 L6 7 L6 4"/></svg>
        600.800.4000
      </div>
      <div class="contact__line">
        <svg class="contact__icon" viewBox="0 0 8 8"><rect x="1" y="3" width="6" height="4"/><path d="M2.5 3 V1 H5.5 V3"/></svg>
        600.800.4000
      </div>
      <div class="contact__line">
        <svg class="contact__icon" viewBox="0 0 8 8"><rect x="0.8" y="1.8" width="6.4" height="4.4"/><path d="M0.8 1.8 L4 4.5 L7.2 1.8"/></svg>
        you@email.com
      </div>
    </address>

    <div class="letterhead__baseline"></div>
  </article>
</main>
</body>
</html>
```